Banner for Vet Hospital 5m x 1.2m - Heat Stroke

Meadowlark Pet Hospital needs a Heat Stroke Banner for Summer.
The banner will be 5000mm long and 1200mm tall.

Our region has been hot this year and this summer is going to be extremely hot.
I want to warn people about heat stroke.
I want you to create a heat stroke banner that conveys the symptoms of heat stroke.

Pictures are better than words.
There should be IMAGES and WORDS that can be seen from the road 30m away and maybe some smaller words for people to read as they walk past.

Here are some of the signs of Heat Stroke:
- Panting which increases as heatstroke progresses
- Drooling, salivating
- Agitation, restlessness
- Very red or pale gums
- Bright red tongue
- Increased heart rate
- Breathing distress
- Vomiting Diarrhea (possibly with blood)
- Signs of mental confusion, delirium
- Dizziness, staggering
- Lethargy, weakness
- Muscle tremors
- Seizures
- Collapsing and lying down
- Little to no urine production
- Coma

I have attached characters that we often use in our advertising. They are optional.
I have done a mock up of the design I imagine. You could refine this design or make your own....or both.

Target Market(s)

Women aged 20 to 50.

Industry/Entity Type

Veterinary

Font styles to use
Sans Serif

Colors
fbed22
f78f20
ec1f27
ffffff

Requirements
Must have
• Heat Stroke Symtpms.
• Heat Stroke Warning.
• Summer theme.
Nice to have
• Bright colours.

```html
<!DOCTYPE html>
<html lang="en">
<head>
<meta charset="utf-8">
<title>Heat Stroke – Summer Warning Banner</title>
<link rel="stylesheet" href="https://fonts.googleapis.com/css2?family=Kalam:wght@400;700&display=swap">
<style>
  :root {
    --sky-orange: #f75a0a;
    --cloud-white: #ffffff;
    --fence-yellow: #e9cb14;
    --fence-shade: #d6b80e;
    --grass-green: #6f9a2c;
    --ground-yellow: #fbed6a;
    --ink: #111111;
    --arrow-orange: #f7690f;
    --bulldog-tone: #ddd3c8;
    --mountain-dog-tone: #2b2622;
    --retriever-tone: #d8b283;
  }
  * { margin: 0; padding: 0; box-sizing: border-box; }
  html, body { width: 1200px; height: 288px; overflow: hidden; background: var(--cloud-white); }
  .banner {
    position: relative;
    width: 1200px;
    height: 288px;
    overflow: hidden;
    font-family: "Kalam", "Comic Sans MS", cursive;
    color: var(--ink);
    background: var(--cloud-white);
  }
  .sky-band { position: absolute; left: 0; top: 0; width: 1200px; height: 142px; }
  .fence { position: absolute; left: 0; top: 142px; width: 1200px; height: 90px; }
  .ground { position: absolute; left: 0; top: 230px; width: 1200px; height: 58px; background: var(--ground-yellow); }
  .grass { position: absolute; left: 0; top: 222px; width: 1200px; height: 12px; background: var(--grass-green); }

  .title {
    position: absolute;
    left: 0; width: 1200px; top: 2px;
    text-align: center;
    font-size: 58px;
    line-height: 1;
    color: var(--cloud-white);
    font-weight: 400;
    letter-spacing: 1px;
  }

  .symptom { position: absolute; line-height: 1; white-space: nowrap; }
  .symptom--small { font-size: 13px; }
  .symptom--medium { font-size: 19px; }
  .symptom--large { font-size: 24px; font-weight: 700; }
  .symptom--xlarge { font-size: 30px; font-weight: 700; }

  .stage-arrow { position: absolute; width: 50px; height: 48px; }

  .dog { position: absolute; }
</style>
</head>
<body>
<main class="banner">
  <svg class="sky-band" viewBox="0 0 1200 142" role="img" aria-label="Orange summer sky with a border of white clouds">
    <defs>
      <linearGradient id="sky-fade" x1="0" y1="0" x2="0" y2="1">
        <stop offset="0" stop-color="var(--sky-orange)"/>
        <stop offset="0.42" stop-color="var(--sky-orange)"/>
        <stop offset="0.72" stop-color="#fbd6c2"/>
        <stop offset="1" stop-color="var(--cloud-white)"/>
      </linearGradient>
    </defs>
    <rect width="1200" height="142" fill="url(#sky-fade)"/>
  </svg>

  <svg class="fence" viewBox="0 0 1200 90" role="img" aria-label="Yellow wooden picket fence">
    <rect width="1200" height="90" fill="var(--fence-yellow)"/>
  </svg>
  <div class="ground"></div>
  <div class="grass" role="img" aria-label="Strip of green grass"></div>

  <h1 class="title">Heat Stroke</h1>

  <p class="symptom symptom--small" style="left:4px; top:116px;">Agitation</p>
  <p class="symptom symptom--medium" style="left:50px; top:90px;">Excessive panting</p>
  <p class="symptom symptom--small" style="left:152px; top:121px;">Drooling</p>
  <p class="symptom symptom--xlarge" style="left:524px; top:95px;">confusion</p>
  <p class="symptom symptom--large" style="left:810px; top:101px;">muscles tremors</p>
  <p class="symptom symptom--large" style="left:1054px; top:101px;">collapse</p>
  <p class="symptom symptom--medium" style="left:302px; top:179px;">Breathing Distress</p>
  <p class="symptom symptom--large" style="left:782px; top:176px;">Coma</p>
  <p class="symptom symptom--large" style="left:378px; top:245px;">Diarrhea</p>
  <p class="symptom symptom--medium" style="left:700px; top:255px;">vomiting</p>

  <svg class="stage-arrow" style="left:226px; top:168px;" viewBox="0 0 50 48" aria-hidden="true">
    <polygon points="0,0 50,24 0,48 14,24" fill="var(--arrow-orange)"/>
  </svg>
  <svg class="stage-arrow" style="left:697px; top:168px;" viewBox="0 0 50 48" aria-hidden="true">
    <polygon points="0,0 50,24 0,48 14,24" fill="var(--arrow-orange)"/>
  </svg>

  <svg class="dog" style="left:0; top:132px;" width="240" height="140" viewBox="0 0 240 140" role="img" aria-label="Photo of a panting white bulldog lying down">
    <rect x="0" y="0" width="240" height="140" rx="40" fill="var(--bulldog-tone)"/>
  </svg>
  <svg class="dog" style="left:540px; top:152px;" width="156" height="132" viewBox="0 0 156 132" role="img" aria-label="Photo of a tired tricolour mountain dog lying flat">
    <rect x="0" y="0" width="156" height="132" rx="36" fill="var(--mountain-dog-tone)"/>
  </svg>
  <svg class="dog" style="left:876px; top:150px;" width="294" height="126" viewBox="0 0 294 126" role="img" aria-label="Photo of a golden retriever collapsed on its side">
    <rect x="0" y="0" width="294" height="126" rx="40" fill="var(--retriever-tone)"/>
  </svg>
</main>
</body>
</html>
```